Wilderness Doc & TV personality personal page

I’m a wilderness and EMS emergency physician with particular sub specialties and a TV show. I need a website to highlight my interviews, teachings, etc... I did buy a number of domains for now.
Topics and things I need: CV (or version) me in the media, picture gallery, actually I sort of really like what dr ned harlow, my colleague has setup plus I have tv show and stuff like that. pinecrest rover dot com

Target Market(s)

EMS, education, commercial products...

Industry/Entity Type

Medical And Science

Coding

Coded - Design and coding required

Number of Pages Required

1 page

Font styles to use
Sans Serif

Colors
f37122
9bcb3c
0556a4
a54499

Requirements
Must have
• Links and photos to news articles and things that mention me that I can add in.
Nice to have
• Maybe some snapshots of lecture reviews or patient thank you notes. Accolades so to speak
• I really appreciate how sharp it is. I would love to see Headings that resemble my friend's at pinecrest rover dot com. Home, experience, consulting, lectures, affiliates, contact... those are main subjects... I think media also and that will have the TV show stuff and articles written about me...then maybe at the bottom of main page also have splits for training, research, television, and maybe exploration
Should not have
• The medical symbol with two snakes... that means quack doctor

```html
<!DOCTYPE html>
<html lang="en">
<head>
<meta charset="utf-8">
<title>Ridgeline MD — Wilderness &amp; EMS Physician</title>
<link href="https://fonts.googleapis.com/css2?family=Oswald:wght@400;500;600&family=Open+Sans:wght@400;600;700&display=swap" rel="stylesheet">
<style>
:root{
  --purple:#a54499;
  --orange:#f37122;
  --green:#9bcb3c;
  --blue:#0556a4;
  --ink:#2d2d2d;
  --text:#555;
  --muted:#8a8a8a;
  --light:#f3f3f3;
  --taupe:#a08c7e;
  --footer:#2a2a2a;
  --white:#fff;
}
*{box-sizing:border-box;margin:0;padding:0}
html,body{width:1200px;height:3866px;overflow:hidden}
body{font-family:"Open Sans",Arial,sans-serif;color:var(--text);background:var(--white);position:relative}
.heading{font-family:"Oswald","Arial Narrow",sans-serif;font-weight:500;color:var(--ink);text-transform:uppercase;letter-spacing:.3px}
.btn{display:inline-block;background:var(--green);color:#1d2a08;font-weight:700;font-size:12px;text-transform:uppercase;padding:0 16px;line-height:31px;text-decoration:none}
.ph{display:block}

/* header */
.site-header{position:absolute;top:0;left:0;width:1200px;height:52px;background:var(--purple);border-bottom:2px solid #c06ab6}
.badge{position:absolute;left:88px;top:8px;width:66px;height:68px;background:#e0312e;color:#fff;font-family:"Oswald",sans-serif;font-size:13px;line-height:15px;text-align:center;padding-top:10px;z-index:2}
.brand{position:absolute;left:172px;top:15px;font-family:"Open Sans",sans-serif;font-weight:600;font-size:19px;color:var(--white);letter-spacing:.5px}
.main-nav{position:absolute;left:457px;top:0;display:flex;height:52px;align-items:center}
.main-nav a{color:#fff;text-decoration:none;font-size:11px;text-transform:uppercase;margin-right:47px}
.search{position:absolute;left:1090px;top:17px}

.hero{position:absolute;top:54px;left:0;width:1200px;height:528px;background:linear-gradient(180deg,#7cc443 0%,#5fae33 70%,#8d8d8d 100%)}
.hero-strip{position:absolute;top:582px;left:0;width:1200px;height:18px;background:#9a9a9a}

/* intro band */
.intro{position:absolute;top:600px;left:0;width:1200px;height:192px;background:var(--orange);text-align:center;color:#fff}
.intro h1{font-family:"Oswald",sans-serif;font-weight:500;font-size:38px;color:#fff;margin-top:30px;line-height:1.2}
.intro p{font-size:16px;margin-top:4px}
.intro .btn{margin-top:14px;font-size:12px;line-height:32px;padding:0 24px}

/* about */
.about{position:absolute;top:850px;left:94px;width:1013px;height:290px}
.about h2{font-size:35px;line-height:45px;width:500px}
.about p{font-size:13.5px;line-height:22.5px;width:510px;color:#888;margin-top:12px}
.about .btn{position:absolute;left:0;top:258px}
.about .video{position:absolute;left:543px;top:6px;width:470px;height:283px;background:linear-gradient(135deg,#c9c4bd,#8e8a85 60%,#6d5a45)}
.play{position:absolute;width:52px;height:52px;border-radius:50%;background:#fff;left:209px;top:115px}
.play::after{content:"";position:absolute;left:21px;top:17px;border-left:14px solid var(--orange);border-top:9px solid transparent;border-bottom:9px solid transparent}

/* popular */
.section-title{position:absolute;left:0;width:1200px;text-align:center;font-size:36px}
.show-grid{position:absolute;left:94px;top:1266px;width:1013px;display:grid;grid-template-columns:repeat(4,244px);column-gap:12.5px;row-gap:0}
.show-card{height:261px}
.show-card .thumb{position:relative;height:153px;background:linear-gradient(135deg,#a6a6a6,#7b7b7b)}
.show-card .thumb::before{content:"";position:absolute;left:105px;top:60px;width:34px;height:34px;border-radius:50%;background:rgba(255,255,255,.45)}
.show-card .thumb::after{content:"";position:absolute;left:119px;top:71px;border-left:9px solid #fff;border-top:6px solid transparent;border-bottom:6px solid transparent}
.show-card h3{font-weight:400;font-size:15.5px;color:#333;margin-top:10px}
.show-card p{font-size:10.5px;color:#777;margin-top:3px}
.meta{font-size:10px;color:#444;margin-top:14px;display:flex;gap:18px}
.meta .star{color:#f5a623}
.meta .plus{color:var(--green)}

/* feature banner */
.feature{position:absolute;top:1818px;left:0;width:1200px;height:394px;background:linear-gradient(90deg,#e9e6e2 0%,#d8d0c8 40%,var(--taupe) 52%,var(--taupe) 100%)}
.feature .portrait{position:absolute;left:0;top:0;width:570px;height:394px;background:linear-gradient(90deg,#ebe8e4,#cfc6bd 70%,#b3a497)}
.feature h2{position:absolute;left:593px;top:70px;width:540px;font-size:35px;line-height:45px;color:#fff}
.feature p{position:absolute;left:593px;top:172px;width:520px;font-size:13.5px;line-height:22.5px;color:#f1ece8}
.feature .btn{position:absolute;left:593px;top:282px}

/* gallery */
.gallery{position:absolute;left:94px;top:2356px;width:1013px;display:grid;grid-template-columns:repeat(4,1fr);gap:3px}
.gallery .ph{height:166px}
.g1{background:linear-gradient(135deg,#d9dee6,#4a5a74)}
.g2{background:linear-gradient(135deg,#e6e6e6,#3c6fa8)}
.g3{background:linear-gradient(135deg,#2d4c84,#d8d8d8)}
.g4{background:linear-gradient(135deg,#e4e4e4,#2f4f86)}

/* news */
.news{position:absolute;top:2755px;left:0;width:1200px;height:485px;background:var(--light)}
.news .section-title{top:40px}
.news-grid{position:absolute;left:94px;top:98px;display:grid;grid-template-columns:repeat(3,325px);column-gap:18px}
.news-card .ph{height:215px}
.n1{background:linear-gradient(135deg,#dcdcdc,#c8312f 70%,#7a1d1d)}
.n2{background:linear-gradient(135deg,#2b2b2b,#8a6a2c 60%,#1d1d1d)}
.n3{background:linear-gradient(180deg,#6aa0d6,#d7c22a 60%,#4a4a4a)}
.news-card h3{font-weight:400;font-size:16px;color:#333;margin-top:14px}
.news-card p{font-size:12px;line-height:18px;color:#777;margin-top:6px;width:300px}
.news-card .btn{margin-top:12px;line-height:29px}
.arrow{position:absolute;top:192px;width:34px;height:34px;border-radius:50%;border:1px solid #ccc;background:#fff;font-size:16px;color:#444;text-align:center;line-height:30px}

/* social */
.social{position:absolute;top:3240px;left:0;width:1200px;height:265px;background:var(--orange);color:#fff;text-align:center}
.social h2{font-family:"Oswald",sans-serif;font-weight:500;font-size:36px;margin-top:40px;color:#fff}
.social-list{position:absolute;left:94px;top:106px;display:flex;width:1013px;justify-content:space-between;list-style:none}
.social-list li{width:186px;text-align:center;font-size:12px;line-height:18px;color:#ffe7d8}
.social-list .dot{display:block;width:64px;height:64px;border-radius:50%;background:#fff;margin:0 auto 14px}

/* footer */
.site-footer{position:absolute;top:3505px;left:0;width:1200px;height:361px;background:var(--footer);color:#9a9a9a;font-size:11px}
.site-footer h4{font-family:"Oswald",sans-serif;font-weight:400;font-size:18px;color:#ddd;text-transform:uppercase}
.f-about{position:absolute;left:94px;top:50px;width:230px}
.f-brand{font-weight:600;font-size:19px;color:#fff}
.f-about p{line-height:19px;margin-top:10px}
.f-about .contact{margin-top:18px;color:#ccc}
.f-links{position:absolute;left:378px;top:52px}
.f-links ul{list-style:none;margin-top:10px}
.f-links li{line-height:23px}
.f-news{position:absolute;left:538px;top:52px;width:240px}
.f-news .field{height:26px;background:#3a3a3a;margin-top:8px;color:#ddd;font-size:9px;line-height:26px;padding-left:10px}
.f-news .field:first-of-type{margin-top:14px}
.f-news .sub{margin-top:12px;height:27px;background:var(--green);color:#1d2a08;font-weight:700;font-size:11px;text-align:center;line-height:27px}
.f-media{position:absolute;left:855px;top:52px;width:260px}
.media-item{display:flex;margin-top:10px;height:53px}
.media-item:first-of-type{margin-top:14px}
.media-item .ph{width:68px;height:53px;flex:none;background:linear-gradient(135deg,#5a7fb0,#c43a2d)}
.media-item div{padding-left:10px;font-size:9px;line-height:12px}
.media-item strong{display:block;font-weight:400;font-size:12px;color:#ddd;line-height:16px}
.media-item em{font-style:normal;color:var(--green)}
.f-bottom{position:absolute;left:94px;top:295px;width:1013px;border-top:1px solid #3c3c3c;text-align:center;font-size:9px;padding-top:22px;color:#888}
.f-bottom b{color:var(--green);font-weight:700}
</style>
</head>
<body>

<header class="site-header">
  <div class="badge">FIRST<br>TIME<br>HERE?</div>
  <div class="brand">Ridgeline MD</div>
  <nav class="main-nav">
    <a href="#">Podcast</a><a href="#">Blog</a><a href="#">Event</a><a href="#">Contact us</a><a href="#">My story</a>
  </nav>
  <svg class="search" width="16" height="16" viewBox="0 0 16 16" fill="none" stroke="#fff" stroke-width="1.6"><circle cx="6.5" cy="6.5" r="4.8"/><line x1="10" y1="10" x2="14.5" y2="14.5"/></svg>
</header>

<div class="hero" role="img" aria-label="Illustration of a TV news studio with camera operators and two anchors at a news desk on a green screen"></div>
<div class="hero-strip"></div>

<section class="intro">
  <h1>I’M A WILDERNESS &amp;</h1>
  <p>EMS emergency physician with particular sub specialties and a TV show.</p>
  <a class="btn" href="#">Subscribe</a>
</section>

<section class="about">
  <h2 class="heading">The standard lorem ipsum used since</h2>
  <p>Sed ut perspiciatis unde omnis iste natus error sit voluptatem accusantium doloremque laudantium, totam rem aperiam, eaque ipsa quae ab illo inventore veritatis et quasi architecto beatae vitae dicta sunt explicabo. Nemo enim ipsam voluptatem quia voluptas sit aspernatur aut odit aut fugit.</p>
  <p>Sed ut perspiciatis unde omnis iste natus error sit voluptatem accusantium doloremque laudantium, totam rem aperiam...</p>
  <a class="btn" href="#">Watch more</a>
  <div class="video" role="img" aria-label="Video still of three doctors in a consultation at a desk"><span class="play"></span></div>
</section>

<h2 class="heading section-title" style="top:1192px">Popular show</h2>
<div class="show-grid">
  <article class="show-card"><div class="thumb" role="img" aria-label="Episode still of doctors in discussion"></div><h3>The Last Month Of particular</h3><p>Sed ut perspiciatis unde omnis...</p><div class="meta"><span><span class="star">★</span> 9.6/10</span><span><span class="plus">+</span> Watchlist</span></div></article>
  <article class="show-card"><div class="thumb" role="img" aria-label="Episode still of a doctor talking with a businessman"></div><h3>The Last Month Of particular</h3><p>Sed ut perspiciatis unde omnis...</p><div class="meta"><span><span class="star">★</span> 9.6/10</span><span><span class="plus">+</span> Watchlist</span></div></article>
  <article class="show-card"><div class="thumb" role="img" aria-label="Episode still of a medical consultation"></div><h3>The Last Month Of particular</h3><p>Sed ut perspiciatis unde omnis...</p><div class="meta"><span><span class="star">★</span> 9.6/10</span><span><span class="plus">+</span> Watchlist</span></div></article>
  <article class="show-card"><div class="thumb" role="img" aria-label="Episode still of doctors reviewing notes"></div><h3>The Last Month Of particular</h3><p>Sed ut perspiciatis unde omnis...</p><div class="meta"><span><span class="star">★</span> 9.6/10</span><span><span class="plus">+</span> Watchlist</span></div></article>
  <article class="show-card"><div class="thumb" role="img" aria-label="Episode still of a doctor reviewing an x-ray"></div><h3>The Last Month Of particular</h3><p>Sed ut perspiciatis unde omnis...</p><div class="meta"><span><span class="star">★</span> 9.6/10</span><span><span class="plus">+</span> Watchlist</span></div></article>
  <article class="show-card"><div class="thumb" role="img" aria-label="Episode still of doctors in discussion"></div><h3>The Last Month Of particular</h3><p>Sed ut perspiciatis unde omnis...</p><div class="meta"><span><span class="star">★</span> 9.6/10</span><span><span class="plus">+</span> Watchlist</span></div></article>
  <article class="show-card"><div class="thumb" role="img" aria-label="Episode still of a medical consultation"></div><h3>The Last Month Of particular</h3><p>Sed ut perspiciatis unde omnis...</p><div class="meta"><span><span class="star">★</span> 9.6/10</span><span><span class="plus">+</span> Watchlist</span></div></article>
  <article class="show-card"><div class="thumb" role="img" aria-label="Episode still of a doctor talking with a businessman"></div><h3>The Last Month Of particular</h3><p>Sed ut perspiciatis unde omnis...</p><div class="meta"><span><span class="star">★</span> 9.6/10</span><span><span class="plus">+</span> Watchlist</span></div></article>
</div>

<section class="feature">
  <div class="portrait" role="img" aria-label="Photo of a presenter in a suit speaking and gesturing"></div>
  <h2 class="heading" style="color:#fff">The standard lorem ipsum passage used since</h2>
  <p>Sed ut perspiciatis unde omnis iste natus error sit voluptatem accusantium doloremque laudantium, totam rem aperiam, eaque ipsa quae ab illo inventore veritatis et quasi architecto beatae vitae dicta sunt explicabo. Nemo enim ipsam voluptatem quia voluptas sit aspernatur aut odit aut fugit.</p>
  <a class="btn" href="#">Read more</a>
</section>

<h2 class="heading section-title" style="top:2294px">Picture gallery</h2>
<div class="gallery">
  <div class="ph g1" role="img" aria-label="Lecture hall audience facing a projection screen"></div>
  <div class="ph g2" role="img" aria-label="Audience member raising a hand during a talk"></div>
  <div class="ph g3" role="img" aria-label="Speaker with a microphone addressing an audience"></div>
  <div class="ph g4" role="img" aria-label="Speaker presenting to a seated audience"></div>
  <div class="ph g3" role="img" aria-label="Speaker with a microphone in a conference hall"></div>
  <div class="ph g4" role="img" aria-label="Audience listening to a presenter"></div>
  <div class="ph g1" role="img" aria-label="Conference room with a projection screen"></div>
  <div class="ph g2" role="img" aria-label="Question from the audience at a lecture"></div>
</div>

<section class="news">
  <h2 class="heading section-title">Latest news</h2>
  <span class="arrow" style="left:30px">‹</span>
  <span class="arrow" style="left:1136px">›</span>
  <div class="news-grid">
    <article class="news-card"><div class="ph n1" role="img" aria-label="Paramedic kneeling beside a medical bag at a scene"></div><h3>The standard Lorem Ipsum passage</h3><p>Sed ut perspiciatis unde omnis iste natus error sit voluptatem accusantium doloremque</p><a class="btn" href="#">Read more</a></article>
    <article class="news-card"><div class="ph n2" role="img" aria-label="Firefighters walking at a night scene"></div><h3>The standard Lorem Ipsum passage</h3><p>Sed ut perspiciatis unde omnis iste natus error sit voluptatem accusantium doloremque</p><a class="btn" href="#">Read more</a></article>
    <article class="news-card"><div class="ph n3" role="img" aria-label="Air ambulance helicopter landed beside an ambulance"></div><h3>The standard Lorem Ipsum passage</h3><p>Sed ut perspiciatis unde omnis iste natus error sit voluptatem accusantium doloremque</p><a class="btn" href="#">Read more</a></article>
  </div>
</section>

<section class="social">
  <h2>STAY TOUCH WITH ME</h2>
  <ul class="social-list">
    <li><span class="dot"></span>Sed ut perspiciatis unde omnis iste natus</li>
    <li><span class="dot"></span>Sed ut perspiciatis unde omnis iste natus</li>
    <li><span class="dot"></span>Sed ut perspiciatis unde omnis iste natus</li>
    <li><span class="dot"></span>Sed ut perspiciatis unde omnis iste natus</li>
    <li><span class="dot"></span>Sed ut perspiciatis unde omnis iste natus</li>
  </ul>
</section>

<footer class="site-footer">
  <div class="f-about">
    <div class="f-brand">Ridgeline MD</div>
    <p>Sed ut perspiciatis unde omnis iste natus error sit voluptatem accusantium doloremque laudantium, totam rem aperiam</p>
    <p class="contact">+1 (555) 014 2290</p>
    <p class="contact" style="margin-top:12px">hello@ridgelinemd.example</p>
  </div>
  <div class="f-links">
    <h4>Quick links</h4>
    <ul><li>Home</li><li>Podcast</li><li>Blog</li><li>Event</li><li>Contact us</li><li>My story</li></ul>
  </div>
  <div class="f-news">
    <h4>Newsletter</h4>
    <div class="field">Name:</div>
    <div class="field">Email:</div>
    <div class="sub">SUBSCRIBE</div>
  </div>
  <div class="f-media">
    <h4>Media</h4>
    <div class="media-item"><span class="ph" role="img" aria-label="Helicopter rescue thumbnail"></span><div><strong>Sed ut perspiciatis unde omnis</strong>iste natus error sit voluptatem<br><em>READ MORE</em></div></div>
    <div class="media-item"><span class="ph" role="img" aria-label="Paramedic at work thumbnail"></span><div><strong>Sed ut perspiciatis unde omnis</strong>iste natus error sit voluptatem<br><em>READ MORE</em></div></div>
    <div class="media-item"><span class="ph" role="img" aria-label="Firefighters at night thumbnail"></span><div><strong>Sed ut perspiciatis unde omnis</strong>iste natus error sit voluptatem<br><em>READ MORE</em></div></div>
  </div>
  <div class="f-bottom">COPYRIGHT © 2019 <b>RIDGELINE MD</b>. ALL RIGHTS RESERVED.</div>
</footer>

</body>
</html>
```